Webbanner-Design für Führungskräfte-Coach
Danke für Ihr Engagement und die einwandfreie Abwicklung.
Zielgruppe
Ich coache Führungskräfte und Teams im Verkauf. Haupt-Keywort und Haupt-Thema:
Führung im Vertrieb. Das Design soll Führungskräften mit Verkaufsfunktionen gefallen.
Aufgabenstellung
Gemäss Memo (Datei: RBF-Banner-Memo).

```html
<!DOCTYPE html>
<html lang="de">
<head>
<meta charset="utf-8">
<title>Riedmann Coaching &amp; Training – Banner</title>
<link rel="stylesheet" href="https://fonts.googleapis.com/css2?family=Arimo:wght@400;700&display=swap">
<style>
  :root {
    --sky-top: #2f7fd0;
    --sky-mid: #5b9fe0;
    --sky-low: #a9cdf0;
    --stripe-blue: #3a72c8;
    --stripe-red: #b0131c;
    --footer: #2e2e2e;
    --white: #ffffff;
    --portrait-light: rgba(70, 90, 115, 0);
    --portrait-dark: #2a3038;
    --cloud: rgba(244, 248, 253, 0.95);
    --cloud-soft: rgba(244, 248, 253, 0.5);
    --cloud-none: rgba(244, 248, 253, 0);
  }
  html, body { margin: 0; padding: 0; overflow: hidden; }
  body { width: 1200px; height: 457px; font-family: "Arimo", Arial, sans-serif; }
  .banner {
    position: relative; width: 1200px; height: 457px; overflow: hidden;
    background: linear-gradient(180deg, var(--sky-top) 0%, var(--sky-mid) 45%, var(--sky-low) 100%);
  }
  .top-stripe { position: absolute; top: 0; left: 0; width: 100%; height: 7px; display: flex; }
  .top-stripe .blue { width: 616px; background: var(--stripe-blue); }
  .top-stripe .red { flex: 1; background: var(--stripe-red); }

  .brand { position: absolute; left: 40px; top: 26px; display: flex; align-items: center; color: var(--white); }
  .brand-square { width: 68px; height: 68px; background: var(--white); opacity: .9; }
  .brand-divider { width: 2px; height: 78px; background: var(--white); margin: 0 9px 0 8px; }
  .brand-name { font-size: 27px; font-weight: 700; line-height: 1.05; }
  .brand-sub { font-size: 23px; font-weight: 400; line-height: 1.2; }

  .headline {
    position: absolute; right: 36px; top: 63px; margin: 0;
    color: var(--white); font-size: 27.5px; font-weight: 700; line-height: 1.2;
  }

  .cloud-arrow {
    position: absolute; left: 80px; top: 87px; width: 490px; height: 275px;
    background: radial-gradient(closest-side, var(--cloud) 0%, var(--cloud-soft) 50%, var(--cloud-none) 100%);
  }

  .portrait {
    position: absolute; left: 703px; top: 128px; width: 326px; height: 283px;
    background: linear-gradient(180deg, var(--portrait-light) 0%, rgba(60, 72, 88, .55) 35%, var(--portrait-dark) 75%);
  }

  .footer {
    position: absolute; left: 0; bottom: 0; width: 100%; height: 46px;
    background: var(--footer); color: var(--white);
    font-size: 21px; font-weight: 700;
  }
  .contact { display: flex; align-items: center; gap: 10px; position: absolute; top: 0; height: 46px; }
  .contact.web { left: 40px; }
  .contact.mail { left: 256px; }
  .contact svg { display: block; }
</style>
</head>
<body>
<div class="banner">
  <div class="top-stripe"><div class="blue"></div><div class="red"></div></div>

  <div class="brand">
    <div class="brand-square"></div>
    <div class="brand-divider"></div>
    <div class="brand-text">
      <div class="brand-name">Riedmann</div>
      <div class="brand-sub">Coaching &amp; Training GmbH</div>
    </div>
  </div>

  <h1 class="headline">Coach für Führungskräfte und Teams im Vertrieb</h1>

  <div class="cloud-arrow" role="img" aria-label="Weisse Wolke in Form eines nach oben zeigenden Pfeils am blauen Himmel"></div>

  <div class="portrait" role="img" aria-label="Porträtfoto des Coaches"></div>

  <div class="footer">
    <div class="contact web">
      <svg width="18" height="18" viewBox="0 0 18 18" fill="none" stroke="#fff" stroke-width="1.6">
        <circle cx="9" cy="9" r="7.5"/><ellipse cx="9" cy="9" rx="3.2" ry="7.5"/><line x1="1.5" y1="9" x2="16.5" y2="9"/>
      </svg>
      <span>www.rbf.ch</span>
    </div>
    <div class="contact mail">
      <svg width="20" height="15" viewBox="0 0 20 15">
        <rect x="0" y="0" width="20" height="15" fill="#fff"/>
        <polyline points="0.5,0.8 10,8.5 19.5,0.8" fill="none" stroke="#2e2e2e" stroke-width="1.6"/>
      </svg>
      <span>Info@rbf.ch</span>
    </div>
  </div>
</div>
</body>
</html>
```